Web design for upcoming direct placement agency

So were looking for a very modern, simple but professional look. We would like to have the site able to translate into 4 different languages- a few idea sites you can reference would be
www.lorvanteam.com **our favorite**
www.brightmeadowfolk.org

We want to ensure the website is tailored to both our clients as well as potential candidates. We want our clients and candidates to understand that we are dedicated to making sure that we want to build relationships with them and that we want to do everything possible to make sure they succeed.

We'd like to steer away from too many up close photos of people. Instead you could try a shadowed view or distant photo that limits the directness.

we have a domain name- www.talvinharbourllc.com

We will upload our business plan as well as a sample business proposal so you have an idea of the information we would like to include.

Target Market(s)

Business' looking to outsource their hiring needs for upper level positions such as but not limited to quality engineers, logistics managers, material managers, etc

Industry/Entity Type

Employment Agency

Number of Pages Required

3 page

Font styles to use
Serif
Sans Serif
Script
Other font styles liked:
• Kennedy Sm Caps

Colors
1b1b1b
9d9d9d
e9e9e9
eeeeee
dadada
0255a3
85acd3
474747

Requirements
Must have
• -ability to translate to English, Spanish, German, and Japanese.
• -Our logo
• -A contact us section
• -Resume upload area
Should not have
• -A job search area
• -pricing info

```html
<!DOCTYPE html>
<html lang="en">
<head>
<meta charset="utf-8">
<title>Talvin Harbour — Executive Placement</title>
<link href="https://fonts.googleapis.com/css2?family=Oswald:wght@400;500&family=Roboto:wght@300;400;500&family=Open+Sans:wght@400;600&display=swap" rel="stylesheet">
<style>
:root{
  --ink:#1b1b1b;
  --ink-deep:#121212;
  --grey:#9d9d9d;
  --grey-dark:#474747;
  --light:#e9e9e9;
  --light-2:#eeeeee;
  --line:#dadada;
  --blue:#0255a3;
  --blue-soft:#85acd3;
  --white:#ffffff;
}
*{box-sizing:border-box;margin:0;padding:0}
html,body{width:1200px;height:2592px;overflow:hidden;background:var(--white)}
body{font-family:"Open Sans",Arial,sans-serif;color:var(--grey-dark);position:relative}

/* header */
.site-header{position:absolute;top:0;left:0;width:1200px;height:120px;background:var(--white);display:flex;align-items:center;justify-content:space-between;padding:0 72px 0 60px}
.brand{display:flex;align-items:center;gap:14px;font-family:"Roboto",sans-serif;font-weight:500;font-size:34px;color:var(--blue)}
.brand-dot{width:26px;height:26px;border-radius:50%;background:var(--blue)}
.main-nav{display:flex;align-items:center;gap:6px;font-family:"Roboto",sans-serif;font-size:17px;color:var(--grey-dark);letter-spacing:.5px}
.main-nav a{padding:14px 16px;text-decoration:none;color:inherit}
.main-nav a.is-active{background:var(--blue);color:var(--white)}
.lang-select{margin-left:10px;background:var(--line);padding:12px 18px;display:flex;gap:8px;align-items:center;color:var(--grey-dark)}

/* hero */
.hero{position:absolute;top:120px;left:0;width:1200px;height:620px}
.hero-photo{position:absolute;inset:0;background:linear-gradient(100deg,#3a3b3d 0%,#6f7174 28%,#bfc1c3 52%,#e6e6e6 70%,#a7a9ab 100%)}
.hero-copy{position:absolute;left:80px;top:120px}
.hero-title{font-family:"Oswald",sans-serif;font-weight:500;font-size:44px;line-height:58px;color:var(--white);letter-spacing:1.5px;text-transform:uppercase}
.btn-search{margin-top:40px;display:inline-flex;height:60px;font-family:"Roboto",sans-serif;font-size:30px;color:var(--white)}
.btn-search span{background:var(--blue);padding:0 26px;display:flex;align-items:center}
.btn-search i{background:var(--ink);width:60px;display:flex;align-items:center;justify-content:center}
.hero-chevron{position:absolute;left:550px;top:578px;width:100px;height:100px;border-radius:50%;background:var(--white);display:flex;align-items:flex-start;justify-content:center;padding-top:20px}

/* proposal */
.proposal{position:absolute;top:740px;left:0;width:1200px;height:388px;text-align:center}
.section-title{font-family:"Roboto",sans-serif;font-weight:400;color:var(--blue);font-size:50px}
.proposal .section-title{margin-top:62px}
.proposal p{width:820px;margin:26px auto 0;font-size:16px;line-height:26px;color:var(--grey-dark)}
.btn-outline{display:inline-block;margin-top:34px;border:2px solid var(--blue);border-radius:30px;padding:10px 30px;font-family:"Roboto",sans-serif;font-size:18px;color:var(--blue);letter-spacing:1px}

/* features */
.features{position:absolute;top:1128px;left:0;width:1200px;height:472px}
.features-photo{position:absolute;inset:0;background:linear-gradient(90deg,#6d7073 0%,#3b3c3e 22%,#242526 45%,#1e1f20 100%)}
.feature{position:absolute;top:80px;width:220px;text-align:center;color:var(--white)}
.feature svg{display:block;margin:0 auto;height:90px}
.feature h3{margin-top:30px;font-family:"Roboto",sans-serif;font-weight:400;font-size:28px;letter-spacing:1px}
.feature p{margin-top:16px;font-size:14px;line-height:22px;color:var(--line)}

/* upload */
.upload{position:absolute;top:1600px;left:0;width:1200px;height:372px;text-align:center;background:var(--white)}
.upload .section-title{margin-top:50px}
.upload p{width:880px;margin:34px auto 0;font-family:"Roboto",sans-serif;font-weight:300;font-size:28px;line-height:40px;color:var(--grey-dark)}
.btn-solid{display:inline-block;margin-top:34px;background:var(--blue);border-radius:34px;padding:16px 36px;font-family:"Roboto",sans-serif;font-size:26px;color:var(--white)}

/* values banner */
.values{position:absolute;top:1972px;left:0;width:1200px;height:288px}
.values-photo{position:absolute;inset:0;background:linear-gradient(90deg,#2a2b2c 0%,#4a4b4d 50%,#2c2d2e 100%)}
.values h2{position:absolute;left:0;right:0;top:106px;text-align:center;font-family:"Oswald",sans-serif;font-weight:400;font-size:58px;letter-spacing:3px;color:var(--white)}

/* footer */
.site-footer{position:absolute;top:2260px;left:0;width:1200px;height:272px;background:var(--ink);color:var(--white)}
.footer-col{position:absolute;top:56px}
.footer-col h4{font-family:"Roboto",sans-serif;font-weight:400;font-size:26px}
.contact-item{display:flex;align-items:center;gap:18px;margin-top:26px;font-size:17px;color:var(--light)}
.contact-item svg{width:22px;height:22px;flex:none}
.newsletter-input{margin-top:28px;width:314px;height:42px;border:1px solid var(--grey);background:var(--ink);color:var(--grey);font-size:15px;padding:0 12px;display:flex;align-items:center}
.btn-subscribe{margin-top:20px;display:inline-block;background:var(--blue);padding:10px 22px;font-family:"Roboto",sans-serif;font-size:17px;letter-spacing:1px}
.footer-bar{position:absolute;top:2532px;left:0;width:1200px;height:60px;background:var(--ink-deep);color:var(--grey);font-size:15px;display:flex;align-items:center;justify-content:center}
.footer-bar b{color:var(--blue-soft);font-weight:400;margin-right:6px}
</style>
</head>
<body>

<header class="site-header">
  <div class="brand"><span class="brand-dot"></span>Talvin Harbour</div>
  <nav class="main-nav">
    <a class="is-active">HOME</a><a>ABOUT</a><a>SERVICES</a><a>BUSINESS PLAN</a><a>JOBS</a><a>CONTACT</a>
    <span class="lang-select">EN
      <svg width="12" height="8" viewBox="0 0 12 8"><path d="M1 1l5 5 5-5" fill="none" stroke="#474747" stroke-width="2"/></svg>
    </span>
  </nav>
</header>

<section class="hero">
  <div class="hero-photo" role="img" aria-label="Overhead view of a team meeting around a white table"></div>
  <div class="hero-copy">
    <h1 class="hero-title">Support professional<br>relationships with<br>each of our customers</h1>
    <div class="btn-search"><span>Search Job</span><i>
      <svg width="20" height="28" viewBox="0 0 20 28"><path d="M4 3l11 11-11 11" fill="none" stroke="#fff" stroke-width="4"/></svg></i></div>
  </div>
  <div class="hero-chevron">
    <svg width="30" height="18" viewBox="0 0 30 18"><path d="M3 3l12 12 12-12" fill="none" stroke="#474747" stroke-width="4"/></svg>
  </div>
</section>

<section class="proposal">
  <h2 class="section-title">Proposal for Executive Placement Services</h2>
  <p>Here at Talvin Harbour we believe in building lasting relationships with our customers. We started out as a family owned business, and we strive to working only the best of the best within our industry. We know there are many people seeking work with the economy's growth and we are determined to provide our clients with only the best.</p>
  <span class="btn-outline">READ MORE</span>
</section>

<section class="features">
  <div class="features-photo" role="img" aria-label="Dark office backdrop with a hand pointing at a glowing button"></div>
  <div class="feature" style="left:338px">
    <svg viewBox="0 0 90 90" aria-hidden="true"><rect x="8" y="56" width="14" height="26" fill="#fff"/><rect x="30" y="44" width="14" height="38" fill="#fff"/><rect x="52" y="32" width="14" height="50" fill="#fff"/><path d="M8 40L36 20 50 28 80 8" fill="none" stroke="#fff" stroke-width="5"/><path d="M68 6h14v14" fill="none" stroke="#fff" stroke-width="5"/></svg>
    <h3>OUR BUSINESS</h3>
    <p>There are many staffing agencies and recruitment business in the market today, but for Talvin Harbour that means nothing.</p>
  </div>
  <div class="feature" style="left:618px">
    <svg viewBox="0 0 110 90" aria-hidden="true"><path d="M6 30l22-10 18 8 16-8 20 4 22 8-8 24-18 18-12 4-22-12-18-10z" fill="#fff"/><path d="M40 46l16 10M48 40l18 12" stroke="#2a2b2c" stroke-width="3"/></svg>
    <h3>MARKETING</h3>
    <p>Most of our advertisement will come from word of mouth by exceeding our customer needs and expectations.</p>
  </div>
  <div class="feature" style="left:898px">
    <svg viewBox="0 0 90 90" aria-hidden="true"><rect x="18" y="6" width="54" height="78" rx="3" fill="none" stroke="#fff" stroke-width="5"/><path d="M28 24h34M28 36h34M28 48h34M28 60h34M28 72h22" stroke="#fff" stroke-width="4"/></svg>
    <h3>APPNDIX</h3>
    <p>Start Up Expenses, Determining Start-Up Capital, Cash Flow, Income Projection Statement, Profit and Loss Statement.</p>
  </div>
</section>

<section class="upload">
  <h2 class="section-title">Upload Your Resume</h2>
  <p>Ensure we are well aware of the requirements each of our customers need from candidates for the position to be filled.</p>
  <span class="btn-solid">Upload Resume</span>
</section>

<section class="values">
  <div class="values-photo" role="img" aria-label="Muted photo of professionals at work"></div>
  <h2>SKILLS. EXPERTISE. EXCELLENCE. DEDICATION</h2>
</section>

<footer class="site-footer">
  <div class="footer-col" style="left:80px">
    <h4>Dana Whitfield</h4>
    <div class="contact-item"><svg viewBox="0 0 22 22"><rect x="6" y="1" width="10" height="20" rx="2" fill="#fff"/><rect x="8" y="4" width="6" height="12" fill="#1b1b1b"/></svg>(555) 706-0146</div>
    <div class="contact-item"><svg viewBox="0 0 22 22"><path d="M5 2l4 0 2 5-3 2c1 3 3 5 6 6l2-3 5 2v4c0 1-1 2-2 2C10 20 2 12 2 4c0-1 1-2 3-2z" fill="#fff"/></svg>(555) 406-0147</div>
    <div class="contact-item"><svg viewBox="0 0 22 22"><rect x="1" y="4" width="20" height="14" fill="none" stroke="#fff" stroke-width="2"/><path d="M1 5l10 8 10-8" fill="none" stroke="#fff" stroke-width="2"/></svg>dwhitfield@talvinharbourllc.com</div>
  </div>
  <div class="footer-col" style="left:440px">
    <h4>Customer Service</h4>
    <div class="contact-item"><svg viewBox="0 0 22 22"><rect x="1" y="4" width="20" height="14" fill="none" stroke="#fff" stroke-width="2"/><path d="M1 5l10 8 10-8" fill="none" stroke="#fff" stroke-width="2"/></svg>service@talvinharbourllc.com</div>
    <div class="brand" style="margin-top:34px;font-size:26px;color:var(--white)">Talvin Harbour</div>
  </div>
  <div class="footer-col" style="left:808px">
    <h4>Newsletter</h4>
    <div class="newsletter-input">Enter Email Id</div>
    <span class="btn-subscribe">SUBSCRIBE</span>
  </div>
</footer>
<div class="footer-bar"><b>© TALVIN HARBOUR</b> - 2015. All Rights Reserved.</div>

</body>
</html>
```